Redesign Video/PIcture Check in Page

Redesign our current TallyPointApp iPhone App checkin screens - Keep the design simple so that programmers do not have to do too much extra work to make your design work. - Look at the attached website screenshot for the overall look and feel, and color scheme - Convert the attached vector logo to iOS Icon format. - Deliver all graphics in the density required for iPhone XS Max. I will upload current check in pages that need to be reimagined. Check in needs to be more intutitive. Would like to add some gamification to the verification screen where they currently are required to enter series of random numbers. simple card game etc might work better. See TallyPointapp in itunes and google play store. also visit vormlink.example or tallypointapp.example for more information about our company.
The Current Checkin Process:
A. Client receives alert to checkin or submits voluntary checkin
B. Clicks checkin button on home Screen.
Redesign from here:
C. Clicks on a check in from check in list screen(new screen)
D. Enters verification number(gamification something better than random numbers)
E. Opens Camera
D. Takes Selfie
F. submits photo
G. clicks check in
SEE CURRENT STEPS PIC I UPLOADED

Target Market(s)

Courts,Probation and parole,Attorneys,Sheriffs,Jails, Alternative sentencing

Colors
3277b5

Requirements
Must have
• Must be easy to navigate,Intuitive!
Nice to have
• Gamification of check in verification.
• Step by step process with next button or similar

```html
<!DOCTYPE html>
<html lang="en">
<head>
<meta charset="utf-8">
<title>TallyPointApp – Check-in Screens</title>
<link href="https://fonts.googleapis.com/css2?family=Catamaran:wght@500;600;700;800&display=swap" rel="stylesheet">
<style>
:root{
  --page-top:#fafafa;
  --page-bottom:#e6e6e8;
  --ink:#111;
  --blue:#3277b5;
  --violet:#9c76b2;
  --screen-top:#4c5661;
  --screen-bottom:#222c36;
  --white:#fff;
  --pill-text:#3a3f46;
  --muted:#9aa0a6;
  --green:#7cc242;
  --success:#7cc23a;
  --failed:#e0622a;
  --pending:#9aa0a8;
  --ring:#8a9199;
  --photo-a:#4b5a7a;
  --photo-b:#1d2233;
  --card-purple:#b47fc0;
  --card-yellow:#e6cf45;
  --pink:#d7265a;
}
*{box-sizing:border-box;margin:0;padding:0}
html,body{width:1200px;height:1200px;overflow:hidden}
body{font-family:"Catamaran",sans-serif;background:linear-gradient(180deg,var(--page-top),var(--page-bottom));position:relative;color:var(--ink)}
.page-title{position:absolute;left:42px;top:22px;font-size:80px;font-weight:800;letter-spacing:-1px;line-height:1}
.screen-label{position:absolute;top:196px;font-size:38px;font-weight:600;line-height:1}
.phone{position:absolute;top:250px;width:345px;height:746px;overflow:hidden;background:linear-gradient(180deg,var(--screen-top),var(--screen-bottom))}
.app-bar{position:absolute;left:0;top:0;width:100%;height:46px;background:linear-gradient(90deg,var(--blue) 40%,var(--violet));color:var(--white);font-size:22px;font-weight:600;text-align:center;line-height:48px}
.home-bar{position:absolute;left:0;bottom:0;width:100%;height:46px;background:linear-gradient(90deg,var(--blue) 40%,var(--violet));z-index:3}
.home-bar::after{content:"";position:absolute;left:110px;top:34px;width:124px;height:4px;border-radius:2px;background:var(--white)}
.pill{position:absolute;top:55px;height:29px;border-radius:10px;background:var(--white);color:var(--pill-text);font-size:15px;font-weight:600;line-height:31px;text-align:center;box-shadow:0 2px 3px rgba(0,0,0,.3)}
.pill.small{font-size:12px}
.abs{position:absolute}
.center-text{text-align:center;color:var(--white)}
/* home */
.battery-chip{left:7px;top:95px;width:79px;height:27px;border-radius:8px;background:var(--white)}
.battery-chip .cell{position:absolute;left:9px;top:7px;width:30px;height:13px;border:1px solid #555;border-radius:2px;background:var(--green)}
.battery-chip .pct{position:absolute;left:47px;top:6px;font-size:8px;font-weight:700}
.bracelet-caption{left:7px;top:126px;width:79px;font-size:8px;font-weight:700;color:var(--white);text-align:center}
.avatar-ring{left:86px;top:90px;width:172px;height:172px;border-radius:50%;background:var(--ring)}
.avatar-photo{position:absolute;left:12px;top:12px;width:148px;height:148px;border-radius:50%;background:radial-gradient(circle at 50% 40%,var(--photo-a),var(--photo-b))}
.user-name{left:0;top:266px;width:100%;font-size:22px;font-weight:600}
.tile-icon{border-radius:50%;background:radial-gradient(circle at 40% 35%,#fff,#e3e3e3);box-shadow:0 3px 6px rgba(0,0,0,.35)}
.tile-icon.big{width:112px;height:112px}
.tile-icon.mid{width:84px;height:84px}
.tile-icon svg{width:100%;height:100%}
.tile-label{width:170px;font-weight:600;color:var(--white);text-align:center}
.tile-label.big{font-size:25px}
.tile-label.mid{font-size:18px}
/* check-in */
.datetime{left:7px;top:121px;width:330px;height:31px;border-radius:14px;background:var(--white);display:flex;font-size:18px;font-weight:600;color:var(--pill-text);line-height:33px}
.datetime span{flex:1;text-align:center}
.datetime span+span{border-left:1px solid #ccc}
.title-band{left:7px;top:159px;width:330px;height:43px;border-radius:16px;background:linear-gradient(90deg,var(--blue),var(--violet));color:var(--white);font-size:25px;font-weight:600;text-align:center;line-height:47px}
.prompt{left:0;top:217px;width:100%;font-size:14px;font-weight:700;color:var(--white);text-align:center}
.code-card{top:239px;width:97px;height:126px;border-radius:6px;background:var(--white);padding:5px}
.code-card .art{position:relative;width:100%;height:100%;background:linear-gradient(135deg,var(--card-purple) 20%,var(--card-yellow) 45%,var(--card-yellow) 60%,var(--card-purple) 85%);text-align:center;line-height:1}
.code-card .small-line{display:block;padding-top:44px;font-size:11px;font-weight:700;color:#111}
.code-card .big-line{display:block;font-size:21px;font-weight:800;color:#111}
.field{left:118px;width:250px;height:35px;border-radius:14px;background:var(--white);color:var(--muted);font-size:16px;font-weight:600;line-height:38px;padding-left:12px;margin-left:-44px}
.field-label{left:74px;font-size:13px;font-weight:700;color:var(--white)}
.selfie-frame{left:118px;top:511px;width:108px;height:108px}
.check-btn{left:146px;top:627px;width:52px;height:52px;border-radius:50%;background:var(--white)}
.check-caption{left:0;top:680px;width:100%;font-size:11px;font-weight:600;color:var(--white);text-align:center}
/* history */
.history-list{position:absolute;left:7px;top:110px;width:330px}
.history-item{position:relative;height:74px;margin-bottom:9px;border-radius:16px;background:linear-gradient(90deg,#5f6fb8,#6a74ba 60%,#7c78b9);box-shadow:0 3px 4px rgba(0,0,0,.35);color:var(--white)}
.history-item .meta{position:absolute;left:17px;top:10px;font-size:14px;font-weight:600;color:#d6d9ee}
.history-item .meta i{font-style:normal;margin:0 9px;opacity:.6}
.history-item .name{position:absolute;left:17px;top:33px;font-size:25px;font-weight:600;white-space:nowrap}
.status{position:absolute;right:16px;top:10px;width:78px;height:19px;border-radius:9px;font-size:12px;font-weight:600;text-align:center;line-height:21px;color:var(--white)}
.status.success{background:var(--success)}
.status.failed{background:var(--failed)}
.status.pending{background:var(--pending);color:#3c4148}
</style>
</head>
<body>
<h1 class="page-title">Revision 1</h1>
<div class="screen-label" style="left:30px">1. Home</div>
<div class="screen-label" style="left:435px">2. Check-in</div>
<div class="screen-label" style="left:840px;top:192px">3. Check-in History</div>

<!-- Home -->
<section class="phone" style="left:30px">
  <div class="app-bar">TallyPointApp</div>
  <div class="pill" style="left:7px;width:79px">≡ HOME</div>
  <div class="pill small" style="left:259px;width:78px">SIGN OUT</div>
  <div class="abs battery-chip"><span class="cell"></span><span class="pct">100%</span></div>
  <div class="abs bracelet-caption">My Bracelet</div>
  <div class="abs avatar-ring"><div class="avatar-photo" role="img" aria-label="Profile photo of the client"></div></div>
  <div class="abs user-name center-text">Marcus T Delaney</div>

  <div class="abs tile-icon big" style="left:38px;top:314px" role="img" aria-label="Bracelet device illustration">
    <svg viewBox="0 0 112 112"><ellipse cx="56" cy="76" rx="34" ry="12" fill="#2f4a66"/><ellipse cx="56" cy="70" rx="30" ry="9" fill="#dfe6ee"/><path d="M48 48a12 12 0 0 1 16 0M42 40a22 22 0 0 1 28 0M36 32a32 32 0 0 1 40 0" stroke="#2b3440" stroke-width="4" fill="none" stroke-linecap="round"/></svg>
  </div>
  <div class="abs tile-icon big" style="left:200px;top:314px">
    <svg viewBox="0 0 112 112"><path d="M28 58l20 20 38-44" stroke="#6cc23a" stroke-width="13" fill="none" stroke-linecap="round" stroke-linejoin="round"/></svg>
  </div>
  <div class="abs tile-label big" style="left:9px;top:428px">BRACELET</div>
  <div class="abs tile-label big" style="left:171px;top:428px">CHECK IN</div>

  <div class="abs tile-icon mid" style="left:52px;top:470px" role="img" aria-label="Map illustration">
    <svg viewBox="0 0 84 84"><circle cx="42" cy="42" r="34" fill="#6c6fb8"/></svg>
  </div>
  <div class="abs tile-icon mid" style="left:214px;top:470px">
    <svg viewBox="0 0 84 84"><rect x="20" y="40" width="9" height="26" fill="#e0622a"/><rect x="32" y="20" width="9" height="46" fill="#e0622a"/><rect x="44" y="32" width="9" height="34" fill="#e0622a"/><rect x="56" y="38" width="9" height="28" fill="#e0622a"/></svg>
  </div>
  <div class="abs tile-label mid" style="left:9px;top:556px">MAPS</div>
  <div class="abs tile-label mid" style="left:171px;top:556px">MY STATS</div>

  <div class="abs tile-icon mid" style="left:52px;top:581px">
    <svg viewBox="0 0 84 84"><circle cx="42" cy="30" r="11" fill="#d7265a"/><path d="M22 62a20 16 0 0 1 40 0z" fill="#d7265a"/></svg>
  </div>
  <div class="abs tile-icon mid" style="left:214px;top:581px">
    <svg viewBox="0 0 84 84"><circle cx="46" cy="20" r="5" fill="#8a58b0"/><path d="M34 36l10-3-6 28c-1 4 3 5 6 2" stroke="#8a58b0" stroke-width="6" fill="none" stroke-linecap="round"/></svg>
  </div>
  <div class="abs tile-label mid" style="left:9px;top:668px">PROFILE</div>
  <div class="abs tile-label mid" style="left:171px;top:668px">INFORMATION</div>
  <div class="home-bar"></div>
</section>

<!-- Check-in -->
<section class="phone" style="left:427px">
  <div class="app-bar">TallyPointApp</div>
  <div class="pill" style="left:7px;width:99px">≡ CHECK IN</div>
  <div class="pill small" style="left:259px;width:78px">CANCEL</div>
  <div class="abs datetime"><span>30 Oct 2018</span><span>14:50:23</span></div>
  <div class="abs title-band">Voluntary Check-In Request</div>
  <div class="abs prompt">Please Select One of These Card to get Code:</div>
  <div class="abs code-card" style="left:18px"><div class="art" role="img" aria-label="Star card artwork"><span class="small-line">Your Code</span><span class="big-line">Here!</span></div></div>
  <div class="abs code-card" style="left:124px"><div class="art" role="img" aria-label="Star card artwork"><span class="small-line">Your Code</span><span class="big-line">Here!</span></div></div>
  <div class="abs code-card" style="left:230px"><div class="art" role="img" aria-label="Star card artwork"><span class="small-line">Your Code</span><span class="big-line">Here!</span></div></div>
  <div class="abs field" style="top:378px">Type the above code</div>
  <div class="abs field-label" style="top:423px">Comment:</div>
  <div class="abs field" style="top:442px">Type to reply</div>
  <div class="abs field-label" style="top:491px">Take your Selfie:</div>
  <svg class="abs selfie-frame" viewBox="0 0 108 108">
    <path d="M2 24V2h24M82 2h24v24M106 84v22H82M26 106H2V84" stroke="#fff" stroke-width="3" fill="none"/>
    <rect x="8" y="8" width="92" height="92" fill="#fff"/>
    <circle cx="54" cy="36" r="16" fill="#d7265a"/>
    <path d="M24 86a30 26 0 0 1 60 0z" fill="#d7265a"/>
  </svg>
  <svg class="abs check-btn" viewBox="0 0 52 52"><path d="M14 27l9 9 16-18" stroke="#4a78c2" stroke-width="5" fill="none" stroke-linecap="round" stroke-linejoin="round"/></svg>
  <div class="abs check-caption">CHECK IN</div>
  <div class="home-bar"></div>
</section>

<!-- Check-in History -->
<section class="phone" style="left:826px">
  <div class="app-bar">TallyPointApp</div>
  <div class="pill" style="left:7px;width:165px">≡ CHECK IN HISTORY</div>
  <div class="pill small" style="left:258px;width:79px">REFRESH</div>
  <div class="history-list">
    <div class="history-item"><span class="meta">30 Oct 2018<i>|</i>14:50:23</span><span class="status pending">PENDING</span><span class="name">Voluntary Check-In Request</span></div>
    <div class="history-item"><span class="meta">29 Oct 2018<i>|</i>16:49:54</span><span class="status success">SUCCESS</span><span class="name">Voluntary Check-In Request</span></div>
    <div class="history-item"><span class="meta">29 Oct 2018<i>|</i>16:49:54</span><span class="status failed">FAILED</span><span class="name">Voluntary Check-In Request</span></div>
    <div class="history-item"><span class="meta">27 Oct 2018<i>|</i>10:51:39</span><span class="status success">SUCCESS</span><span class="name">Voluntary Check-In Request</span></div>
    <div class="history-item"><span class="meta">27 Oct 2018<i>|</i>10:49:27</span><span class="status success">SUCCESS</span><span class="name">Voluntary Check-In Request</span></div>
    <div class="history-item"><span class="meta">26 Oct 2018<i>|</i>17:59:50</span><span class="status success">SUCCESS</span><span class="name">Voluntary Check-In Request</span></div>
    <div class="history-item"><span class="meta">26 Oct 2018<i>|</i>17:58:44</span><span class="status success">SUCCESS</span><span class="name">Voluntary Check-In Request</span></div>
    <div class="history-item"><span class="meta">25 Oct 2018<i>|</i>09:12:05</span><span class="status success">SUCCESS</span><span class="name">Voluntary Check-In Request</span></div>
  </div>
  <div class="home-bar" style="background:linear-gradient(90deg,var(--blue) 40%,var(--violet))"></div>
</section>
</body>
</html>
```